3D printers services needs a brochure

We need a Creative, Innovative idea for a brochure. 3d printing for Prototyping, .
We would like to have an A4 horizontal brochure that could give a 3D effect when folded or cut.
Our name is K7! Spark! Build! Soar! our website is www.k7momentum.com. Please be inspired by our logo and the dreamy cloud part.
Our prospects: Architects, Artists, Museums and Designers ( Jewellery, watches, etc ...)
What we offer:
.3D printing and prototyping.
.3D scanning.
.Transforming 2D images to 3D objects.
. Making their Portals where clients can visualize, personalize (IN 3D) and order their work.

Reason: I would like to extend it because i figured out the deadline is too short! Thank you Best regards Fadri

Printing

```html
<!DOCTYPE html>
<html lang="en">
<head>
<meta charset="utf-8">
<title>K7 Momentum – 3D Printing Flyer</title>
<link href="https://fonts.googleapis.com/css2?family=Anton&family=Oswald:wght@500;700&family=Questrial&family=Open+Sans:wght@400;600;700&display=swap" rel="stylesheet">
<style>
  :root {
    --paper: #ffffff;
    --green-light: #b9cf3c;
    --green: #8fb02a;
    --green-deep: #5f8a1d;
    --navy: #1f2a6b;
    --ink: #1b1b1b;
    --grey: #6f6f6f;
    --bullet: #9fd02a;
  }
  * { margin: 0; padding: 0; box-sizing: border-box; }
  html, body { width: 925px; height: 1200px; overflow: hidden; background: var(--paper); }
  .flyer { position: relative; width: 925px; height: 1200px; overflow: hidden; background: var(--paper); font-family: "Open Sans", sans-serif; }

  .sky-cloud { position: absolute; left: 40px; top: 200px; }
  .brand { position: absolute; left: 80px; top: 120px; display: flex; align-items: center; gap: 16px; }
  .brand-square { width: 42px; height: 42px; background: var(--green); }
  .brand-name { font-family: "Questrial", sans-serif; font-size: 130px; line-height: 1; color: var(--grey); }

  .hero-visual { position: absolute; left: 480px; top: 45px; width: 410px; height: 310px; }

  .tagline { position: absolute; left: 50px; top: 366px; font-family: "Questrial", sans-serif; font-size: 36px; line-height: 1; letter-spacing: 2px; color: #333; }

  .green-field { position: absolute; left: 0; top: 500px; width: 925px; height: 700px;
    background: radial-gradient(ellipse at 70% 15%, var(--green-light) 0%, var(--green) 60%, var(--green-deep) 100%); }
  .wave { position: absolute; left: 0; top: 420px; width: 925px; height: 120px; }

  .portrait { position: absolute; left: 0; top: 588px; width: 410px; height: 612px;
    background: radial-gradient(ellipse at 45% 35%, #e8c3a8 0%, #c98f6e 45%, #f3c52a 80%, #e9b516 100%);
    border-radius: 180px 180px 0 0; }

  .prospects { position: absolute; left: 350px; top: 586px; width: 520px; text-align: center; color: #fff; }
  .prospects h2 { font-family: "Anton", sans-serif; font-weight: 400; font-size: 50px; line-height: 1.1; letter-spacing: 1px;
    color: #f3f3f3; text-shadow: 0 2px 0 #8a8a8a, 0 3px 4px rgba(0,0,0,.45); }
  .prospects p { font-size: 23px; font-weight: 600; line-height: 1.4; text-shadow: 0 1px 3px rgba(0,0,0,.5); margin-top: 8px; }

  .offer { position: absolute; left: 316px; top: 748px; width: 566px; height: 280px; }
  .offer svg { position: absolute; inset: 0; width: 566px; height: 280px; }
  .offer h3 { position: absolute; left: 188px; top: 22px; width: 200px; text-align: center;
    font-family: "Oswald", sans-serif; font-weight: 700; font-size: 34px; line-height: 1.12; color: var(--navy); }
  .offer ul { position: absolute; left: 52px; top: 116px; width: 490px; list-style: none; }
  .offer li { position: relative; padding-left: 24px; font-size: 16px; font-weight: 600; color: var(--navy); line-height: 1.3; margin-bottom: 9px; }
  .offer li::before { content: ""; position: absolute; left: 0; top: 5px; width: 12px; height: 12px; border-radius: 50%;
    background: radial-gradient(circle at 35% 35%, #e6ff8a, var(--bullet) 60%, #5c8a12); }

  .phone { position: absolute; left: 432px; top: 1030px; font-family: "Oswald", sans-serif; font-weight: 500; font-size: 38px; line-height: 1.1; letter-spacing: 2px; color: var(--ink); }
  .email { position: absolute; left: 450px; top: 1088px; font-size: 15px; line-height: 1.2; font-weight: 700; color: var(--ink); }
  .address { position: absolute; left: 410px; top: 1114px; font-size: 15px; line-height: 1.2; color: var(--ink); }
  .rule { position: absolute; left: 410px; top: 1143px; width: 355px; height: 1px; background: rgba(255,255,255,.85); }
  .web { position: absolute; left: 410px; top: 1150px; font-family: "Oswald", sans-serif; font-weight: 700; font-size: 30px; line-height: 1.2; letter-spacing: 1px; color: #222; }
</style>
</head>
<body>
<main class="flyer">
  <svg class="sky-cloud" width="340" height="190" viewBox="0 0 340 190" aria-hidden="true">
    <defs><linearGradient id="mist" x1="0" y1="0" x2="0" y2="1"><stop offset="0" stop-color="#ffffff"/><stop offset="1" stop-color="#d7dbe0"/></linearGradient></defs>
    <path d="M20 170 C-10 170 0 125 40 125 C40 90 90 80 110 105 C130 55 220 55 235 105 C270 80 330 105 310 150 C340 165 320 188 290 184 L40 186 C20 186 20 178 20 170 Z" fill="url(#mist)"/>
  </svg>

  <div class="brand"><span class="brand-square"></span><span class="brand-name">K7</span></div>

  <svg class="hero-visual" viewBox="0 0 420 330" preserveAspectRatio="none" role="img" aria-label="Rendered 3D architectural floor model framed in a cloud shape">
    <defs><linearGradient id="model" x1="0" y1="0" x2="1" y2="1"><stop offset="0" stop-color="#3b4d5c"/><stop offset=".5" stop-color="#c9d2d8"/><stop offset="1" stop-color="#22303b"/></linearGradient></defs>
    <path d="M40 300 C0 300 -5 230 40 215 C10 160 60 100 110 120 C120 40 220 10 260 60 C300 10 400 40 385 120 C430 150 420 230 370 245 C385 300 330 320 300 300 Z" fill="url(#model)"/>
  </svg>

  <p class="tagline">SPARK! BUILD! SOAR!</p>

  <div class="green-field"></div>
  <svg class="wave" viewBox="0 0 925 120" preserveAspectRatio="none" aria-hidden="true">
    <defs><linearGradient id="swoosh" x1="0" y1="0" x2="1" y2="0"><stop offset="0" stop-color="#6f9b22"/><stop offset=".6" stop-color="#c6d94a"/><stop offset="1" stop-color="#9cbd2d"/></linearGradient></defs>
    <path d="M0 20 C200 90 420 0 640 35 C760 55 860 30 925 20 L925 120 L0 120 Z" fill="url(#swoosh)"/>
    <path d="M0 40 C220 110 430 20 650 55 C770 75 860 55 925 50 L925 120 L0 120 Z" fill="#a9c637"/>
    <path d="M0 50 C230 120 440 35 660 68 C780 85 870 70 925 68" fill="none" stroke="#fff" stroke-width="5"/>
  </svg>

  <div class="portrait" role="img" aria-label="Portrait photo of a smiling woman in a yellow top"></div>

  <section class="prospects">
    <h2>OUR PROSPECTS:</h2>
    <p>Architects, Artists, Museums, Designers<br>(Jewellery, Watches, etc ...)</p>
  </section>

  <section class="offer">
    <svg viewBox="0 0 525 300" preserveAspectRatio="none" aria-hidden="true">
      <defs><radialGradient id="sky" cx=".5" cy=".3" r=".8"><stop offset="0" stop-color="#f4fbff"/><stop offset=".5" stop-color="#a9d8f6"/><stop offset="1" stop-color="#3f8fd0"/></radialGradient></defs>
      <path d="M40 290 C5 290 0 215 35 200 C10 150 60 110 120 130 C140 60 200 20 265 25 C335 30 370 80 365 110 C420 90 490 120 470 170 C525 190 520 270 470 285 Z" fill="url(#sky)" stroke="#d9efff" stroke-width="3"/>
    </svg>
    <h3>What<br>we offer:</h3>
    <ul>
      <li>3D printing and prototyping</li>
      <li>3D scanning</li>
      <li>Transforming 2D images to 3D objects</li>
      <li>Making their Portals where clients can visualize,<br>personalize (IN 3D) and order their work.</li>
    </ul>
  </section>

  <p class="phone">+4179 555 0172</p>
  <p class="email">E-mail : Fadri@K7momentum.org</p>
  <p class="address">Rue des Alpes 48, Lausanne 1003 Switzerland</p>
  <div class="rule"></div>
  <p class="web">www.k7momentum.com</p>
</main>
</body>
</html>
```